Professional Business Cards for Janitorial Company

We are a Janitorial Company that services Commercial Buildings.

Our Logo is included. It can't look silly or cartoonish. Has to look professional.

Information:
Derek Hollin
Operations Manager
760.413.2987
DHollin@BrightwayServicesPV.com
www.BrightwayServicesPV.com

```html
<!DOCTYPE html>
<html lang="en">
<head>
<meta charset="utf-8">
<title>Brightway Services – Business Cards</title>
<link rel="stylesheet" href="https://fonts.googleapis.com/css2?family=Open+Sans:wght@400;600;700&display=swap">
<style>
  :root {
    --stage: #7a5f42;
    --brand-blue: #2bbce6;
    --card-white: #ffffff;
    --charcoal: #414141;
    --muted: #d6d6d6;
  }
  * { margin: 0; padding: 0; box-sizing: border-box; }
  html, body { width: 1200px; height: 803px; overflow: hidden; }
  body {
    background: var(--stage);
    font-family: "Open Sans", Arial, sans-serif;
    position: relative;
  }
  .card {
    position: absolute;
    top: 250px;
    width: 525px;
    height: 300px;
    border-radius: 22px;
    overflow: hidden;
    box-shadow: 0 10px 24px rgba(0,0,0,0.35);
  }
  .card--front { left: 50px; background: var(--brand-blue); }
  .card--back { left: 625px; background: var(--card-white); }
  .card__art { position: absolute; inset: 0; }

  /* Front */
  .brand-mark {
    position: absolute;
    display: flex;
    align-items: center;
    gap: 12px;
    font-weight: 700;
    line-height: 1.05;
  }
  .brand-mark__square {
    width: 58px; height: 58px;
    border-radius: 6px;
  }
  .card--front .brand-mark { left: 120px; top: 62px; color: var(--card-white); font-size: 30px; }
  .card--front .brand-mark__square { background: var(--card-white); }
  .front-url {
    position: absolute;
    left: 78px; top: 212px;
    color: var(--card-white);
    font-size: 15px;
    font-weight: 600;
  }

  /* Back */
  .card--back .brand-mark { right: 40px; top: 58px; color: var(--brand-blue); font-size: 24px; }
  .card--back .brand-mark__square { background: var(--brand-blue); width: 46px; height: 46px; }
  .contact {
    position: absolute;
    left: 60px; top: 120px;
    color: var(--card-white);
  }
  .contact__name { font-size: 17px; font-weight: 700; }
  .contact__title { font-size: 11px; color: var(--muted); margin-bottom: 12px; }
  .contact__list { list-style: none; }
  .contact__item {
    display: flex; align-items: center; gap: 10px;
    font-size: 13px; line-height: 21px;
  }
  .contact__icon { width: 12px; height: 12px; flex: none; }
</style>
</head>
<body>

<section class="card card--front" aria-label="Card front">
  <svg class="card__art" viewBox="0 0 525 300" aria-hidden="true">
    <rect x="0" y="160" width="190" height="12" fill="#ffffff"/>
    <rect x="120" y="176" width="305" height="6" fill="#ffffff"/>
    <rect x="340" y="262" width="185" height="12" fill="#ffffff"/>
  </svg>
  <div class="brand-mark">
    <span class="brand-mark__square"></span>
    <span>Brightway<br>Services</span>
  </div>
  <p class="front-url">www.BrightwayServicesPV.com</p>
</section>

<section class="card card--back" aria-label="Card back">
  <svg class="card__art" viewBox="0 0 525 300" aria-hidden="true">
    <path d="M0,72 C170,36 360,92 470,300 L438,300 C338,112 160,66 0,92 Z" fill="#2bbce6"/>
    <path d="M0,92 C160,66 338,112 438,300 L0,300 Z" fill="#414141"/>
    <rect x="300" y="116" width="188" height="4" fill="#2bbce6"/>
  </svg>
  <div class="brand-mark">
    <span class="brand-mark__square"></span>
    <span>Brightway<br>Services</span>
  </div>
  <div class="contact">
    <p class="contact__name">Derek Hollin</p>
    <p class="contact__title">Operations Manager</p>
    <ul class="contact__list">
      <li class="contact__item">
        <svg class="contact__icon" viewBox="0 0 24 24"><path fill="#fff" d="M6.6 10.8a15 15 0 0 0 6.6 6.6l2.2-2.2c.3-.3.7-.4 1-.2 1.1.4 2.3.6 3.6.6.6 0 1 .4 1 1V20c0 .6-.4 1-1 1A17 17 0 0 1 3 4c0-.6.4-1 1-1h3.5c.6 0 1 .4 1 1 0 1.3.2 2.5.6 3.6.1.3 0 .7-.2 1z"/></svg>
        <span>760.413.2987</span>
      </li>
      <li class="contact__item">
        <svg class="contact__icon" viewBox="0 0 24 24"><rect x="2" y="5" width="20" height="14" rx="1.5" fill="none" stroke="#fff" stroke-width="2"/><path d="M2 6l10 7 10-7" fill="none" stroke="#fff" stroke-width="2"/></svg>
        <span>DHollin@BrightwayServicesPV.com</span>
      </li>
      <li class="contact__item">
        <svg class="contact__icon" viewBox="0 0 24 24"><circle cx="12" cy="12" r="9.5" fill="none" stroke="#fff" stroke-width="2"/><path d="M2.5 12h19M12 2.5c3 3 3 16 0 19M12 2.5c-3 3-3 16 0 19" fill="none" stroke="#fff" stroke-width="1.6"/></svg>
        <span>www.BrightwayServicesPV.com</span>
      </li>
    </ul>
  </div>
</section>

</body>
</html>
```